Create custom funnel illustration

I've attached 3 files to this project. One is an example of the current design/colors so I'm looking for a design to match the current look & feel.

Second is a section of the website that we want to replace with the new infographic design.

Lastly, is a sample concept of what we're looking for.

Target Market(s)

40+ college educated

Industry/Entity Type

Business Software

Font styles to use
Sans Serif

Requirements
Must have
• Design to match the current look & feel. See "design-sample.png"

```html
<!DOCTYPE html>
<html lang="en">
<head>
<meta charset="utf-8">
<title>Custom Funnel Infographic Design</title>
<link rel="stylesheet" href="https://fonts.googleapis.com/css2?family=Orbitron:wght@800&family=Open+Sans:wght@400;700&display=swap">
<style>
  :root {
    --board: #d9d9d9;
    --panel: #ffffff;
    --navy: #16263f;
    --purple: #6a51ad;
    --purple-dark: #4e3a8c;
    --blue: #4ab0e8;
    --blue-deep: #3a97d6;
    --ink: #1b1b33;
    --muted: #8a8a96;
    --grey-text: #4a4a4a;
    --icon-bg: #f1f1f4;
    --line: #3a3a44;
    --soft-line: #c9c9cf;
  }
  html, body { margin: 0; padding: 0; overflow: hidden; }
  body {
    width: 1200px; height: 2400px; position: relative;
    background: var(--board);
    font-family: "Open Sans", sans-serif;
  }
  .board-title {
    position: absolute; top: 52px; left: 0; width: 1200px; margin: 0;
    text-align: center; color: #ffffff;
    font-family: "Orbitron", sans-serif; font-weight: 800;
    font-size: 70px; line-height: 102px; letter-spacing: -1px;
  }
  .variant {
    position: absolute; left: 32px; width: 1136px; height: 639px;
    background: var(--panel); overflow: hidden;
  }
  .variant svg { display: block; width: 1136px; height: 639px; }
  .variant--classic { top: 309px; }
  .variant--split   { top: 1007px; }
  .variant--bold    { top: 1694px; }
  .label { font-family: "Open Sans", sans-serif; font-weight: 700; fill: var(--ink); text-anchor: middle; }
  .label--tiny { font-weight: 400; font-size: 9px; fill: var(--muted); }
  .funnel-text { font-family: "Open Sans", sans-serif; font-weight: 700; fill: #ffffff; text-anchor: middle; }
  .result { font-family: "Open Sans", sans-serif; font-weight: 700; text-anchor: middle; }
</style>
</head>
<body>
<h1 class="board-title">CUSTOM FUNNEL<br>INFOGRAPHIC DESIGN</h1>

<!-- Variant 1: curved arrows into conical funnel -->
<section class="variant variant--classic">
  <svg viewBox="0 0 1220 686" xmlns="http://www.w3.org/2000/svg">
    <defs>
      <linearGradient id="iconFill" x1="0" y1="0" x2="1" y2="1">
        <stop offset="0" stop-color="#4ab0e8"/><stop offset="1" stop-color="#6a51ad"/>
      </linearGradient>
      <marker id="arrowDark" viewBox="0 0 10 10" refX="8" refY="5" markerWidth="8" markerHeight="8" orient="auto">
        <path d="M0,0 L10,5 L0,10 L3,5 Z" fill="#3a3a44"/>
      </marker>
    </defs>
    <g fill="none" stroke="var(--line)" stroke-width="1.6" marker-end="url(#arrowDark)">
      <path d="M401,186 Q480,200 514,265"/>
      <path d="M480,150 Q558,188 566,262"/>
      <path d="M604,151 L604,262"/>
      <path d="M725,150 Q655,188 645,262"/>
      <path d="M819,186 Q740,198 692,265"/>
    </g>
    <g class="asset-icons">
      <g role="img" aria-label="Real estate building icon"><circle cx="361" cy="186" r="40" fill="var(--icon-bg)"/><circle cx="361" cy="186" r="24" fill="url(#iconFill)"/></g>
      <g role="img" aria-label="Bank icon"><circle cx="456" cy="126" r="40" fill="var(--icon-bg)"/><circle cx="456" cy="126" r="24" fill="url(#iconFill)"/></g>
      <g role="img" aria-label="Stocks and bonds pie chart icon"><circle cx="604" cy="111" r="40" fill="var(--icon-bg)"/><circle cx="604" cy="111" r="24" fill="url(#iconFill)"/></g>
      <g role="img" aria-label="Corporate office building icon"><circle cx="755" cy="126" r="40" fill="var(--icon-bg)"/><circle cx="755" cy="126" r="24" fill="url(#iconFill)"/></g>
      <g role="img" aria-label="Diamond ring icon"><circle cx="859" cy="186" r="40" fill="var(--icon-bg)"/><circle cx="859" cy="186" r="24" fill="url(#iconFill)"/></g>
    </g>
    <g font-size="15">
      <text class="label" x="361" y="120">Real</text><text class="label" x="361" y="137">Estate</text>
      <text class="label" x="456" y="62">Bank</text><text class="label" x="456" y="79">Accounts</text>
      <text class="label" x="604" y="47">Stock &amp;</text><text class="label" x="604" y="64">Bonds</text>
      <text class="label" x="755" y="62">Corporation</text><text class="label" x="755" y="79">LLC</text>
      <text class="label" x="859" y="120">Sole</text><text class="label" x="859" y="137">Prop</text>
    </g>
    <g class="funnel">
      <path d="M441,257 C480,300 560,360 571,523 L651,523 C662,360 742,300 781,257 Z" fill="var(--purple)"/>
      <ellipse cx="611" cy="257" rx="170" ry="33" fill="var(--blue)"/>
      <ellipse cx="611" cy="268" rx="135" ry="22" fill="var(--blue-deep)"/>
      <text class="funnel-text" x="611" y="353" font-size="28">Your</text>
      <text class="funnel-text" x="611" y="385" font-size="28">Modern</text>
      <text class="funnel-text" x="611" y="417" font-size="28">Trust</text>
      <rect x="601" y="445" width="20" height="36" fill="#ffffff"/>
      <path d="M593,481 L629,481 L611,510 Z" fill="var(--blue)"/>
    </g>
    <g role="img" aria-label="Beneficiaries group icon"><rect x="575" y="538" width="72" height="75" rx="6" fill="url(#iconFill)"/></g>
    <text class="result" x="611" y="647" font-size="27" fill="var(--ink)">Trust Beneficiaries</text>
  </svg>
</section>

<!-- Variant 2: dark and light flat funnels -->
<section class="variant variant--split">
  <svg viewBox="0 0 1220 686" xmlns="http://www.w3.org/2000/svg">
    <defs>
      <linearGradient id="iconFill2" x1="0" y1="0" x2="1" y2="1">
        <stop offset="0" stop-color="#4ab0e8"/><stop offset="1" stop-color="#6a51ad"/>
      </linearGradient>
    </defs>
    <rect x="0" y="0" width="501" height="686" fill="var(--navy)"/>
    <!-- dark side -->
    <g stroke="#4a6288" stroke-width="1" fill="none">
      <circle cx="181" cy="156" r="30"/><circle cx="255" cy="117" r="30"/><circle cx="333" cy="160" r="30"/>
      <circle cx="166" cy="229" r="30"/><circle cx="250" cy="189" r="30"/><circle cx="247" cy="252" r="30"/><circle cx="328" cy="247" r="30"/>
    </g>
    <g fill="url(#iconFill2)">
      <circle cx="181" cy="156" r="17" role="img" aria-label="Real estate icon"/>
      <circle cx="255" cy="117" r="17" role="img" aria-label="Stocks pie chart icon"/>
      <circle cx="333" cy="160" r="17" role="img" aria-label="Business interests icon"/>
      <circle cx="166" cy="229" r="17" role="img" aria-label="Bank icon"/>
      <circle cx="250" cy="189" r="17" role="img" aria-label="Retirement chair icon"/>
      <circle cx="247" cy="252" r="17" role="img" aria-label="Insurance umbrella icon"/>
      <circle cx="328" cy="247" r="17" role="img" aria-label="Personal property ring icon"/>
    </g>
    <g stroke="var(--blue)" stroke-width="1" fill="none">
      <path d="M226,115 L226,160 M222,155 L226,160 L230,155"/>
      <path d="M206,195 L206,270 M202,265 L206,270 L210,265"/>
      <path d="M292,155 L292,270 M288,265 L292,270 L296,265"/>
    </g>
    <rect x="143" y="290" width="222" height="14" rx="7" fill="var(--blue)"/>
    <path d="M174,304 L334,304 C300,350 286,400 286,455 L224,455 C224,400 210,350 174,304 Z" fill="var(--purple)"/>
    <text class="funnel-text" x="254" y="347" font-size="19">Your</text>
    <text class="funnel-text" x="254" y="368" font-size="19">Modern</text>
    <text class="funnel-text" x="254" y="390" font-size="19">Trust</text>
    <path d="M255,413 L255,437 M250,431 L255,437 L260,431" stroke="#ffffff" stroke-width="1.2" fill="none"/>
    <rect x="221" y="457" width="66" height="14" rx="6" fill="#ffffff"/>
    <path d="M229,471 L279,471 A25,25 0 0 1 229,471 Z" fill="var(--blue)"/>
    <circle cx="254" cy="478" r="4" fill="#ffffff"/><rect x="249" y="484" width="10" height="8" rx="3" fill="#ffffff"/>
    <g role="img" aria-label="Beneficiaries group icon"><rect x="234" y="514" width="42" height="45" rx="4" fill="url(#iconFill2)"/></g>
    <text class="result" x="261" y="595" font-size="21" fill="#ffffff">Trust Beneficiaries</text>

    <!-- light side -->
    <g fill="none" stroke="var(--soft-line)" stroke-width="1">
      <path d="M658,84 Q735,180 742,284"/>
      <path d="M1031,84 Q955,180 946,284"/>
    </g>
    <g stroke="#e3e3e8" stroke-width="1.5" fill="#ffffff">
      <circle cx="842" cy="53" r="30"/>
      <circle cx="766" cy="135" r="30"/><circle cx="842" cy="135" r="30"/><circle cx="919" cy="135" r="30"/>
      <circle cx="766" cy="225" r="30"/><circle cx="842" cy="225" r="30"/><circle cx="919" cy="225" r="30"/>
    </g>
    <g fill="url(#iconFill2)">
      <circle cx="842" cy="53" r="17" role="img" aria-label="Bank accounts icon"/>
      <circle cx="766" cy="135" r="17" role="img" aria-label="Real estate icon"/>
      <circle cx="842" cy="135" r="17" role="img" aria-label="Retirement chair icon"/>
      <circle cx="919" cy="135" r="17" role="img" aria-label="Insurance umbrella icon"/>
      <circle cx="766" cy="225" r="17" role="img" aria-label="Personal property ring icon"/>
      <circle cx="842" cy="225" r="17" role="img" aria-label="Stocks and bonds pie chart icon"/>
      <circle cx="919" cy="225" r="17" role="img" aria-label="Business interests icon"/>
    </g>
    <text class="label label--tiny" x="842" y="94">Bank Accounts</text>
    <text class="label label--tiny" x="766" y="177">Real Estate</text>
    <text class="label label--tiny" x="842" y="177">Retirement</text>
    <text class="label label--tiny" x="919" y="177">Insurance</text>
    <text class="label label--tiny" x="766" y="267">Personal</text><text class="label label--tiny" x="766" y="278">Property</text>
    <text class="label label--tiny" x="842" y="267">Stocks &amp;</text><text class="label label--tiny" x="842" y="278">Bonds</text>
    <text class="label label--tiny" x="919" y="267">Business</text><text class="label label--tiny" x="919" y="278">interests</text>
    <rect x="732" y="290" width="222" height="14" rx="7" fill="var(--blue)"/>
    <path d="M763,304 L923,304 C889,350 875,400 875,455 L813,455 C813,400 799,350 763,304 Z" fill="var(--purple)"/>
    <text class="funnel-text" x="843" y="347" font-size="19">Your</text>
    <text class="funnel-text" x="843" y="368" font-size="19">Modern</text>
    <text class="funnel-text" x="843" y="390" font-size="19">Trust</text>
    <path d="M844,413 L844,437 M839,431 L844,437 L849,431" stroke="#ffffff" stroke-width="1.2" fill="none"/>
    <rect x="810" y="457" width="66" height="14" rx="6" fill="#c4c4c8"/>
    <path d="M818,471 L868,471 A25,25 0 0 1 818,471 Z" fill="var(--blue)"/>
    <circle cx="843" cy="478" r="4" fill="#ffffff"/><rect x="838" y="484" width="10" height="8" rx="3" fill="#ffffff"/>
    <g role="img" aria-label="Beneficiaries group icon"><rect x="823" y="514" width="42" height="45" rx="4" fill="url(#iconFill2)"/></g>
    <text class="result" x="850" y="595" font-size="21" fill="var(--grey-text)">Trust Beneficiaries</text>
  </svg>
</section>

<!-- Variant 3: bold straight arrows -->
<section class="variant variant--bold">
  <svg viewBox="0 0 1220 686" xmlns="http://www.w3.org/2000/svg">
    <defs>
      <linearGradient id="iconFill3" x1="0" y1="0" x2="1" y2="1">
        <stop offset="0" stop-color="#4ab0e8"/><stop offset="1" stop-color="#6a51ad"/>
      </linearGradient>
    </defs>
    <g stroke-width="4" fill="none" stroke-linecap="round">
      <path d="M448,233 L500,285" stroke="var(--purple)"/><path d="M452,226 L478,252" stroke="var(--blue)"/>
      <path d="M486,285 L500,285 L500,271" stroke="var(--purple)"/>
      <path d="M525,210 L548,270" stroke="var(--purple)"/><path d="M531,206 L543,238" stroke="var(--blue)"/>
      <path d="M536,262 L548,270 L554,257" stroke="var(--purple)"/>
      <path d="M611,186 L611,262" stroke="var(--purple)"/><path d="M611,186 L611,220" stroke="var(--blue)"/>
      <path d="M600,251 L611,262 L622,251" stroke="var(--purple)"/>
      <path d="M697,205 L675,268" stroke="var(--purple)"/><path d="M692,203 L681,235" stroke="var(--blue)"/>
      <path d="M669,255 L675,268 L687,261" stroke="var(--purple)"/>
      <path d="M773,232 L725,282" stroke="var(--purple)"/><path d="M769,226 L745,251" stroke="var(--blue)"/>
      <path d="M725,268 L725,282 L739,282" stroke="var(--purple)"/>
    </g>
    <g class="asset-icons">
      <g role="img" aria-label="Real estate building icon"><circle cx="416" cy="202" r="40" fill="var(--icon-bg)"/><circle cx="416" cy="202" r="24" fill="url(#iconFill3)"/></g>
      <g role="img" aria-label="Bank icon"><circle cx="503" cy="169" r="40" fill="var(--icon-bg)"/><circle cx="503" cy="169" r="24" fill="url(#iconFill3)"/></g>
      <g role="img" aria-label="Stocks and bonds pie chart icon"><circle cx="611" cy="144" r="40" fill="var(--icon-bg)"/><circle cx="611" cy="144" r="24" fill="url(#iconFill3)"/></g>
      <g role="img" aria-label="Corporate office building icon"><circle cx="718" cy="164" r="40" fill="var(--icon-bg)"/><circle cx="718" cy="164" r="24" fill="url(#iconFill3)"/></g>
      <g role="img" aria-label="Diamond ring icon"><circle cx="805" cy="201" r="40" fill="var(--icon-bg)"/><circle cx="805" cy="201" r="24" fill="url(#iconFill3)"/></g>
    </g>
    <g font-size="15">
      <text class="label" x="405" y="137">Real</text><text class="label" x="405" y="154">Estate</text>
      <text class="label" x="495" y="105">Bank</text><text class="label" x="495" y="122">Accounts</text>
      <text class="label" x="606" y="79">Stock &amp;</text><text class="label" x="606" y="96">Bonds</text>
      <text class="label" x="718" y="98">Corporation</text><text class="label" x="718" y="115">LLC</text>
      <text class="label" x="806" y="134">Sole</text><text class="label" x="806" y="151">Prop</text>
    </g>
    <g class="funnel">
      <path d="M484,302 C520,350 580,400 586,514 L651,514 C657,400 718,350 754,302 Z" fill="var(--purple)"/>
      <ellipse cx="619" cy="302" rx="135" ry="28" fill="var(--blue)"/>
      <ellipse cx="619" cy="313" rx="105" ry="18" fill="var(--blue-deep)"/>
      <text class="funnel-text" x="619" y="390" font-size="24">Your</text>
      <text class="funnel-text" x="619" y="415" font-size="24">Modern</text>
      <text class="funnel-text" x="619" y="441" font-size="24">Trust</text>
      <path d="M606,486 L619,498 L632,486" stroke="#2a1f5c" stroke-width="4" fill="none"/>
    </g>
    <g role="img" aria-label="Beneficiaries group icon"><rect x="596" y="534" width="46" height="43" rx="4" fill="url(#iconFill3)"/></g>
    <text class="result" x="619" y="614" font-size="21" fill="var(--ink)">Trust Beneficiaries</text>
  </svg>
</section>
</body>
</html>
```